Quill Harbor Gems Website revamp

Hi,

We need a working WordPress theme, not just a .PSD file. Thank you.

We need a complete revamp of our website. We sell lab grown diamonds online. We sell the idea that everyone should be able to afford a diamond. Thus our diamonds are priced very reasonably. Our selling point "the joy of giving and receiving a diamond in a little box".

Our range of products includes rings, bangles, necklace, ear rings etc. We currently only operate in Singapore. Some photos of our products are on our websites.

Need.
- Clean look and feel, simplistic preferably white and soft colours
- Easy to navigate
- No banners
- E Com
- Introduction page
- Willing to change logo if needed

Existing page: www.quillharborgems-example.com

Target Market(s)

Young ladies
Ladies
Men buying for ladies
Young boyfriends fresh out of school buying for love ones
Working ladies to match what they wear to work

Industry/Entity Type

Online

Requirements
Must have
• ECOM. Product shopping cart
Pictures uploads
Intro page
Nice to have
• Pastel colors preferred. - Color scheme is important in our business to create a long term impression. Color scheme will also be used for next potential project, i.e. packaging design.

Should not have
• Should not have old style fonts.

```html
<!DOCTYPE html>
<html lang="en">
<head>
<meta charset="utf-8">
<title>Quill Harbor Gems</title>
<link rel="stylesheet" href="https://fonts.googleapis.com/css2?family=Signika:wght@300;400;600&family=PT+Sans+Narrow:wght@400;700&display=swap">
<style>
:root{
  --page:#f4f3f0;
  --white:#ffffff;
  --teal:#0a9fbd;
  --teal-dark:#006a80;
  --teal-deep:#004c66;
  --ink:#222222;
  --text:#444444;
  --muted:#9a9a9a;
  --line:#dedede;
  --footer:#e7e7e5;
  --field:#f0f0f0;
}
*{margin:0;padding:0;box-sizing:border-box}
html,body{width:982px;height:1200px;overflow:hidden;background:var(--page)}
body{position:relative;font-family:"Signika",sans-serif;color:var(--text)}
.abs{position:absolute}
.cond{font-family:"PT Sans Narrow",sans-serif;font-weight:700}
.btn-dark{position:absolute;background:var(--ink);color:var(--white);font-family:"PT Sans Narrow",sans-serif;font-weight:700;display:flex;align-items:center;justify-content:center;text-transform:uppercase}
.ph{position:absolute;border-radius:4px}

/* header */
.brand{left:112px;top:36px;display:flex;align-items:center;gap:8px;font-size:22px;font-weight:300;color:#8a9596}
.brand-mark{width:14px;height:14px;border:1px solid #8a9596}
.top-links{right:114px;top:23px;font-size:10.5px;font-weight:300;color:var(--ink)}
.top-links span{margin:0 4px}
.bag{left:745px;top:47px;width:38px;height:41px;background:linear-gradient(#8cc63f,#5a9e1e);border-radius:2px}
.cart-sum{left:791px;top:60px;font-size:12.5px;font-weight:300;color:var(--teal-dark)}

/* nav */
.nav{left:106px;top:100px;width:770px;height:52px;background:linear-gradient(#00819b,#00607a);border-radius:2px}
.nav a{position:absolute;top:18px;font-size:13px;color:var(--white);text-decoration:none;font-family:"PT Sans Narrow",sans-serif;font-weight:700}
.nav .sep{position:absolute;top:0;width:1px;height:52px;background:rgba(0,0,0,.25);box-shadow:1px 0 0 rgba(255,255,255,.12)}
.search{left:558px;top:15px;width:201px;height:21px;background:var(--white);border-radius:2px;font-size:7px;color:var(--muted);padding:6px 7px;font-family:"Signika",sans-serif;font-weight:300}
.search svg{position:absolute;right:5px;top:5px}

/* hero */
.hero{left:106px;top:163px;width:771px;height:249px;background:var(--white);overflow:hidden}
.hero-panel{position:absolute;left:0;top:0}
.hero-copy{position:absolute;left:0;width:290px;text-align:center;color:var(--white);font-weight:300;line-height:1}
.hero-btn{position:absolute;left:90px;top:184px;width:108px;height:32px;background:var(--teal);color:var(--white);font-family:"PT Sans Narrow",sans-serif;font-weight:700;font-size:15px;display:flex;align-items:center;justify-content:center}
.hero-title{position:absolute;left:479px;width:240px;top:51px;text-align:center;font-size:19px;font-weight:300;color:var(--ink)}
.hero-text{position:absolute;left:482px;width:234px;top:84px;text-align:center;font-size:9px;line-height:19.6px;font-weight:300;color:var(--muted)}
.dot{position:absolute;top:220px;width:10px;height:10px;border-radius:50%;background:#555}

/* promos */
.promo{top:429px;width:245px;height:138px;background:var(--white)}
.promo .l1{position:absolute;left:11px;top:45px;font-size:17px;font-weight:300;color:#555}
.promo .l2{position:absolute;left:11px;top:67px;font-size:21px;font-weight:300;color:var(--teal)}
.promo .btn-dark{left:11px;top:104px;width:64px;height:19px;font-size:8.5px}

/* products */
.section-title{top:606px;font-size:21px;font-weight:300;color:var(--ink)}
.arrow{position:absolute;top:604px;width:22px;height:22px;border-radius:50%}
.card{width:181px;height:131px;background:var(--white);border:1px solid var(--line)}
.p-name{font-size:12.5px;color:var(--ink)}
.p-stock{font-size:10px;font-weight:300;color:var(--ink)}
.p-price{font-size:26px;font-weight:600;color:var(--teal);text-align:right;width:100px}
.add{width:89px;height:27px;font-size:11.5px;gap:5px}

/* side */
.side{left:694px;width:182px;background:var(--white);border:1px solid var(--line)}
.field{position:absolute;left:17px;width:147px;height:28px;background:var(--field);font-size:9.5px;font-weight:300;color:var(--muted);padding:8px 6px}

/* footer */
.footer{left:0;top:1117px;width:982px;height:83px;background:var(--footer)}
.foot-links{left:108px;top:18px;font-size:12px;color:var(--ink);font-weight:300}
.foot-links span{margin:0 9px}
.copy{left:108px;top:44px;font-size:11.5px;color:var(--ink);font-weight:300}
.social{top:33px;width:28px;height:28px;border-radius:50%}
</style>
</head>
<body>

<header>
  <div class="abs brand"><span class="brand-mark"></span>Quill Harbor</div>
  <div class="abs top-links">Cart<span>|</span>Checkout<span>|</span>My Account</div>
  <div class="abs bag" role="img" aria-label="Shopping bag"></div>
  <div class="abs cart-sum">0 items - $0</div>
</header>

<nav class="abs nav">
  <a style="left:22px">HOME</a><span class="sep" style="left:71px"></span>
  <a style="left:87px">SHOP</a><span class="sep" style="left:137px"></span>
  <a style="left:153px">OUR STORY</a><span class="sep" style="left:238px"></span>
  <a style="left:256px">OUR DIAMONDS</a><span class="sep" style="left:365px"></span>
  <a style="left:383px">CONTACT US</a><span class="sep" style="left:468px"></span>
  <div class="abs search">Type search
    <svg width="11" height="11" viewBox="0 0 11 11"><circle cx="4.5" cy="4.5" r="3.3" fill="none" stroke="#999" stroke-width="1.2"/><line x1="7" y1="7" x2="10" y2="10" stroke="#999" stroke-width="1.4"/></svg>
  </div>
</nav>

<section class="abs hero">
  <svg class="hero-panel" width="300" height="249" viewBox="0 0 300 249">
    <defs><linearGradient id="heroGrad" x1="0" y1="0" x2="1" y2="1"><stop offset="0" stop-color="#00a6bd"/><stop offset=".55" stop-color="#006b8a"/><stop offset="1" stop-color="#004060"/></linearGradient></defs>
    <polygon points="0,0 287,0 221,249 0,249" fill="url(#heroGrad)"/>
  </svg>
  <div class="hero-copy" style="top:50px;font-size:28px">Quill Harbor</div>
  <div class="hero-copy" style="top:83px;font-size:46px">Special</div>
  <div class="hero-copy" style="top:131px;font-size:32px">Ring Offers</div>
  <div class="hero-btn">SHOP NOW</div>
  <div class="ph" style="left:299px;top:48px;width:160px;height:157px;background:radial-gradient(circle at 50% 55%,#3cc9c0 0%,#9fe3dd 55%,#ffffff 80%)" role="img" aria-label="Turquoise gift box with white ribbon"></div>
  <div class="hero-title">Quill Harbor</div>
  <div class="hero-text">Lorem Ipsum is simply dummy text of the printing and typesetting industry. Lorem Ipsum has been the indus-try's standard dummy text ever since the 1500s, when an unknown printer took a galley</div>
  <div class="btn-dark" style="left:550px;top:176px;width:92px;height:28px;font-size:13px">SHOP NOW</div>
  <span class="dot" style="left:249px;background:var(--teal)"></span>
  <span class="dot" style="left:262px"></span>
  <span class="dot" style="left:275px"></span>
  <span class="dot" style="left:288px"></span>
</section>

<section>
  <div class="abs promo" style="left:106px">
    <div class="l1">Shop for</div><div class="l2">Special Offers</div>
    <div class="btn-dark">SHOP NOW</div>
    <div class="ph" style="left:147px;top:28px;width:95px;height:100px;background:radial-gradient(circle,#d8d8dc 0%,#c9a7d8 30%,#ffffff 72%)" role="img" aria-label="Diamond ring set with violet stone"></div>
  </div>
  <div class="abs promo" style="left:368px">
    <div class="l1">Quill Harbor</div><div class="l2">COLLECTIONS</div>
    <div class="btn-dark">SHOP NOW</div>
    <div class="ph" style="left:140px;top:26px;width:98px;height:86px;background:radial-gradient(circle,#222 0%,#333 45%,#1aa6b0 60%,#ffffff 75%)" role="img" aria-label="Black gift box with turquoise ribbon"></div>
  </div>
  <div class="abs promo" style="left:632px">
    <div class="l1" style="left:20px;top:40px;font-size:20px;color:var(--teal)">15% Offer</div>
    <div class="l2" style="left:17px;top:64px;font-size:20px;color:#444">ON BANGS</div>
    <div class="btn-dark" style="left:19px">SHOP NOW</div>
    <div class="ph" style="left:125px;top:4px;width:115px;height:130px;background:radial-gradient(ellipse,#ffffff 30%,#e9e2c8 50%,#ffffff 70%)" role="img" aria-label="Gold diamond tennis bangle"></div>
  </div>
</section>

<section>
  <h2 class="abs section-title" style="left:103px">Featured Products</h2>
  <svg class="arrow" style="left:629px" viewBox="0 0 22 22"><circle cx="11" cy="11" r="11" fill="#2a8fb0"/><polyline points="13,6 8,11 13,16" fill="none" stroke="#fff" stroke-width="2"/></svg>
  <svg class="arrow" style="left:657px" viewBox="0 0 22 22"><circle cx="11" cy="11" r="11" fill="#0d3e55"/><polyline points="9,6 14,11 9,16" fill="none" stroke="#fff" stroke-width="2"/></svg>
  <h2 class="abs section-title" style="left:696px">Today’s Product</h2>

  <div class="abs card" style="left:106px;top:646px"><div class="ph" style="left:45px;top:20px;width:90px;height:90px;background:radial-gradient(circle,#e4e4e4,#ffffff 70%)" role="img" aria-label="Diamond halo ring"></div></div>
  <div class="abs card" style="left:303px;top:646px"><div class="ph" style="left:55px;top:45px;width:70px;height:35px;background:radial-gradient(ellipse,#bbaaa8,#ffffff 70%)" role="img" aria-label="Diamond eternity band"></div></div>
  <div class="abs card" style="left:500px;top:646px"><div class="ph" style="left:45px;top:15px;width:90px;height:100px;background:radial-gradient(ellipse,#d8dbe0,#ffffff 70%)" role="img" aria-label="Crossover diamond bangle"></div></div>

  <div class="abs p-name cond" style="left:106px;top:792px">THE ONE</div>
  <div class="abs p-stock" style="left:106px;top:810px">1 in stock</div>
  <div class="abs p-price" style="left:187px;top:791px">$550</div>
  <div class="btn-dark add" style="left:107px;top:831px"><svg width="12" height="10" viewBox="0 0 12 10"><path d="M0 1h2l1.5 6h7l1-4H3" fill="none" stroke="#fff" stroke-width="1"/><circle cx="4.5" cy="9" r="1" fill="#fff"/><circle cx="9.5" cy="9" r="1" fill="#fff"/></svg>ADD TO CART</div>

  <div class="abs p-name cond" style="left:303px;top:792px">THE ONE</div>
  <div class="abs p-stock" style="left:303px;top:810px">1 in stock</div>
  <div class="abs p-price" style="left:384px;top:791px">$550</div>
  <div class="btn-dark add" style="left:304px;top:831px"><svg width="12" height="10" viewBox="0 0 12 10"><path d="M0 1h2l1.5 6h7l1-4H3" fill="none" stroke="#fff" stroke-width="1"/><circle cx="4.5" cy="9" r="1" fill="#fff"/><circle cx="9.5" cy="9" r="1" fill="#fff"/></svg>ADD TO CART</div>

  <div class="abs p-name cond" style="left:500px;top:792px">THE ONE</div>
  <div class="abs p-stock" style="left:500px;top:810px">1 in stock</div>
  <div class="abs p-price" style="left:582px;top:791px">$550</div>
  <div class="btn-dark add" style="left:501px;top:831px"><svg width="12" height="10" viewBox="0 0 12 10"><path d="M0 1h2l1.5 6h7l1-4H3" fill="none" stroke="#fff" stroke-width="1"/><circle cx="4.5" cy="9" r="1" fill="#fff"/><circle cx="9.5" cy="9" r="1" fill="#fff"/></svg>ADD TO CART</div>

  <div class="abs card" style="left:106px;top:882px"><div class="ph" style="left:45px;top:20px;width:90px;height:90px;background:radial-gradient(circle,#e4e4e4,#ffffff 70%)" role="img" aria-label="Diamond halo ring"></div></div>
  <div class="abs card" style="left:303px;top:882px"><div class="ph" style="left:55px;top:45px;width:70px;height:35px;background:radial-gradient(ellipse,#bbaaa8,#ffffff 70%)" role="img" aria-label="Diamond eternity band"></div></div>
  <div class="abs card" style="left:500px;top:882px"><div class="ph" style="left:45px;top:15px;width:90px;height:100px;background:radial-gradient(ellipse,#d8dbe0,#ffffff 70%)" role="img" aria-label="Crossover diamond bangle"></div></div>

  <div class="abs p-name cond" style="left:106px;top:1028px">THE ONE</div>
  <div class="abs p-stock" style="left:106px;top:1046px">1 in stock</div>
  <div class="abs p-price" style="left:187px;top:1027px">$550</div>
  <div class="btn-dark add" style="left:107px;top:1066px"><svg width="12" height="10" viewBox="0 0 12 10"><path d="M0 1h2l1.5 6h7l1-4H3" fill="none" stroke="#fff" stroke-width="1"/><circle cx="4.5" cy="9" r="1" fill="#fff"/><circle cx="9.5" cy="9" r="1" fill="#fff"/></svg>ADD TO CART</div>

  <div class="abs p-name cond" style="left:303px;top:1028px">THE ONE</div>
  <div class="abs p-stock" style="left:303px;top:1046px">1 in stock</div>
  <div class="abs p-price" style="left:384px;top:1027px">$550</div>
  <div class="btn-dark add" style="left:304px;top:1066px"><svg width="12" height="10" viewBox="0 0 12 10"><path d="M0 1h2l1.5 6h7l1-4H3" fill="none" stroke="#fff" stroke-width="1"/><circle cx="4.5" cy="9" r="1" fill="#fff"/><circle cx="9.5" cy="9" r="1" fill="#fff"/></svg>ADD TO CART</div>

  <div class="abs p-name cond" style="left:500px;top:1028px">THE ONE</div>
  <div class="abs p-stock" style="left:500px;top:1046px">1 in stock</div>
  <div class="abs p-price" style="left:582px;top:1027px">$550</div>
  <div class="btn-dark add" style="left:501px;top:1066px"><svg width="12" height="10" viewBox="0 0 12 10"><path d="M0 1h2l1.5 6h7l1-4H3" fill="none" stroke="#fff" stroke-width="1"/><circle cx="4.5" cy="9" r="1" fill="#fff"/><circle cx="9.5" cy="9" r="1" fill="#fff"/></svg>ADD TO CART</div>
</section>

<aside>
  <div class="abs side" style="top:646px;height:212px">
    <div class="abs cond" style="left:19px;top:14px;font-size:12.5px;font-weight:400;color:var(--ink)">DROP</div>
    <div class="ph" style="left:52px;top:34px;width:68px;height:77px;background:radial-gradient(ellipse,#dcdcdc,#ffffff 70%)" role="img" aria-label="Diamond drop earrings"></div>
    <div class="abs" style="left:19px;top:115px;width:150px;font-size:10px;line-height:16.4px;font-weight:300;color:var(--text)">Lorem Ipsum is simply dummy text of the printing and typeset-ting industry.</div>
    <div class="btn-dark" style="left:20px;top:174px;width:76px;height:27px;font-size:12px">SHOP NOW</div>
  </div>
  <div class="abs side" style="top:883px;height:210px">
    <div class="abs" style="left:15px;top:15px;font-size:16px;font-weight:300;color:var(--ink)">Sign Up for</div>
    <div class="abs" style="left:14px;top:33px;font-size:16px;font-weight:600;color:var(--teal)">Newsletter</div>
    <div class="abs" style="left:15px;top:59px;width:140px;font-size:9.5px;line-height:16.4px;font-weight:300;color:var(--muted)">Lorem Ipsum is simply dummy text of the printing</div>
    <div class="field" style="top:100px">Enter Name</div>
    <div class="field" style="top:138px">Enter E-mail ID</div>
    <div class="abs" style="left:52px;top:177px;width:67px;height:22px;background:var(--teal);color:var(--white);font-size:9.5px;font-weight:600;display:flex;align-items:center;justify-content:center">Subscribe</div>
  </div>
</aside>

<footer class="abs footer">
  <div class="abs foot-links">Home<span>|</span>Shop<span>|</span>Our story<span>|</span>Our diamonds<span>|</span>Contact Us</div>
  <div class="abs copy">© 2013 Quill Harbor. All Rights Reserved.</div>
  <span class="abs social" style="left:816px;background:#5fc3ea" aria-label="Social link"></span>
  <span class="abs social" style="left:849px;background:#3b5a9a" aria-label="Social link"></span>
</footer>

</body>
</html>
```